SipNOW Business Cards

Hi designers!

Here's some background on our start-up and this project:

SipNOW is a website that will allow users to order alcohol from nearby liquor stores and have it delivered to their homes in minutes. We are really excited to work on creating the best online, alcohol purchasing experience for the users.

So why SipNOW? We like to think of ourselves as that great friend who will get alcohol for you because he happens to have a car. We help you drink in with your friends, family, or guests. Our site will target students and young professionals (of drinking age) who are comfortable buying things online or through apps. We don't see this service as a luxury, VIP, or niche service in the least; instead, we think of us as a relaxed, service-driven start-up that believes in simple design and transparent .

Now, we want a business card that incorporates our newly acquired logo design and some complimenting colors and fonts. Feel free to do it single or double sided, although I'm a sucker for double...

If you happen to have any questions, want to throw some ideas around, or just want some feedback- email me at marco@sipnow.example.

Marco Tessin
Founder

Industry/Entity Type

Business

Requirements
Must have
• Name, Position, Email, Cell-phone

No address, no fax, no land-line.

```html
<!DOCTYPE html>
<html lang="en">
<head>
<meta charset="utf-8">
<title>SipNOW Business Card</title>
<link rel="stylesheet" href="https://fonts.googleapis.com/css2?family=Bebas+Neue&family=Fira+Sans+Condensed:ital,wght@1,400;1,700&display=swap">
<style>
  :root {
    --stage: #2d2d2b;
    --card: #fef7e2;
    --ink: #231f20;
    --amber: #f8c21c;
    --label: #e3e3e3;
    --white: #ffffff;
  }
  html, body {
    margin: 0;
    padding: 0;
    overflow: hidden;
  }
  .canvas {
    position: relative;
    width: 1200px;
    height: 1000px;
    background: var(--stage);
    overflow: hidden;
  }
  .card {
    position: absolute;
    left: 152px;
    width: 876px;
    height: 454px;
    background: var(--card);
  }
  .card--front { top: 29px; }
  .card--back { top: 517px; }

  .side-label {
    position: absolute;
    left: 1038px;
    font-family: "Bebas Neue", sans-serif;
    font-size: 58px;
    line-height: 1;
    color: var(--label);
    letter-spacing: 1px;
  }
  .side-label--front { top: 428px; }
  .side-label--back { top: 916px; }

  .wordmark {
    position: absolute;
    left: 0;
    right: 0;
    top: 150px;
    margin: 0;
    text-align: center;
    font-family: "Bebas Neue", sans-serif;
    font-weight: 400;
    font-size: 150px;
    letter-spacing: 4px;
    line-height: 1;
    color: var(--ink);
  }

  .bottle-art {
    position: absolute;
    left: 238px;
    top: 127px;
    width: 472px;
    height: 127px;
  }
  .name {
    position: absolute;
    left: 246px;
    top: 127px;
    height: 127px;
    margin: 0;
    display: flex;
    align-items: center;
    gap: 6px;
    font-family: "Bebas Neue", sans-serif;
    font-weight: 400;
    line-height: 1;
    color: var(--white);
    white-space: nowrap;
  }
  .name__first {
    font-size: 138px;
  }
  .name__last {
    font-size: 70px;
  }
  .role {
    position: absolute;
    left: 306px;
    top: 250px;
    margin: 0;
    font-family: "Bebas Neue", sans-serif;
    font-weight: 400;
    font-size: 38px;
    letter-spacing: 12px;
    line-height: 1;
    color: var(--amber);
  }
  .contact {
    position: absolute;
    left: 281px;
    top: 285px;
    margin: 0;
    font-family: "Fira Sans Condensed", sans-serif;
    font-style: italic;
    color: var(--ink);
    line-height: 1.05;
  }
  .contact__email {
    display: block;
    font-weight: 700;
    font-size: 26px;
    letter-spacing: 0.5px;
  }
  .contact__phone {
    display: block;
    font-weight: 400;
    font-size: 26px;
    margin-left: 17px;
    letter-spacing: 0.5px;
  }
</style>
</head>
<body>
<main class="canvas">
  <section class="card card--front">
    <h1 class="wordmark">SipNOW</h1>
  </section>
  <span class="side-label side-label--front">Front</span>

  <section class="card card--back">
    <svg class="bottle-art" role="img" aria-label="Amber bottle silhouette behind the name" viewBox="0 0 472 127">
      <rect x="0" y="0" width="472" height="127" rx="4" fill="var(--amber)"/>
    </svg>
    <h2 class="name">
      <span class="name__first">MARCO</span>
      <span class="name__last">TESSIN</span>
    </h2>
    <p class="role">Founder</p>
    <p class="contact">
      <span class="contact__email">marco@sipnow.example</span>
      <span class="contact__phone">(000) 000-0000</span>
    </p>
  </section>
  <span class="side-label side-label--back">Back</span>
</main>
</body>
</html>
```